Women's Clothing / Pip & Tansy's
I'd prefer to have the logo centered at the top of the letterhead and have the address, etc. listed on the bottom. Also, I'm not fond of the little icons that indicate address, phone, email, web. Maybe an envelope with just the logo on the front and the return address on the flap? I think they all look really busy with the big logo in the corner and the address on the bottom. It's something I won't use often, so simple is good.
I really like the front of the business card in #4 and the back of the card in purple. More feedback later on the rest. Thanks for all of the options so far!
Cute design, thanks! What would it look like if the back was purple and the logo was white?

```html
<!DOCTYPE html>
<html lang="en">
<head>
<meta charset="utf-8">
<title>Pip &amp; Tansy's — Business Card</title>
<link href="https://fonts.googleapis.com/css2?family=Source+Sans+3:wght@400;600;700&display=swap" rel="stylesheet">
<style>
  :root {
    --backdrop: #2c2c2c;
    --card: #ffffff;
    --plum: #8c3577;
    --amber: #d98a2b;
    --ink: #3a3a3a;
  }
  * { margin: 0; padding: 0; box-sizing: border-box; }
  html, body {
    width: 1200px;
    height: 780px;
    overflow: hidden;
    background: var(--backdrop);
    font-family: "Source Sans 3", Arial, sans-serif;
  }
  .canvas {
    position: relative;
    width: 1200px;
    height: 780px;
    display: flex;
    align-items: center;
    justify-content: center;
  }
  .business-card {
    position: relative;
    width: 1000px;
    height: 580px;
    background: var(--card);
    border-radius: 34px;
    box-shadow: 0 10px 30px rgba(0,0,0,0.45);
  }
  .brand {
    position: absolute;
    left: 64px;
    top: 70px;
  }
  .brand-name {
    font-size: 66px;
    font-weight: 400;
    color: var(--plum);
    line-height: 1;
    letter-spacing: -0.5px;
  }
  .brand-tagline {
    margin-top: 10px;
    font-size: 17px;
    font-weight: 400;
    letter-spacing: 4.5px;
    color: var(--amber);
    text-transform: uppercase;
  }
  .contact {
    position: absolute;
    left: 64px;
    top: 232px;
    color: var(--ink);
  }
  .person-name {
    font-size: 30px;
    font-weight: 700;
    color: var(--amber);
    line-height: 1.1;
  }
  .person-role {
    font-size: 19px;
    font-weight: 600;
    color: var(--plum);
    margin-top: 2px;
  }
  .address {
    margin-top: 30px;
    font-size: 20px;
    line-height: 1.4;
  }
  .contact-lines {
    margin-top: 26px;
    list-style: none;
    font-size: 20px;
    line-height: 1.75;
  }
  .contact-label {
    font-weight: 700;
    color: var(--plum);
    margin-right: 6px;
  }
  .brand-disc {
    position: absolute;
    left: 580px;
    top: 90px;
    width: 400px;
    height: 400px;
  }
</style>
</head>
<body>
  <main class="canvas">
    <section class="business-card">
      <header class="brand">
        <h1 class="brand-name">Pip &amp; Tansy's</h1>
        <p class="brand-tagline">Apparel • Accessories • Gifts</p>
      </header>

      <div class="contact">
        <p class="person-name">Marla Hensley</p>
        <p class="person-role">Proprietor</p>
        <p class="address">742 North Elm Avenue<br>Oakdale, MN 55128</p>
        <ul class="contact-lines">
          <li><span class="contact-label">T :</span>555-214-7788</li>
          <li><span class="contact-label">E :</span>corbelwrenx@pipandtansys.com</li>
          <li><span class="contact-label">W :</span>www.pipandtansys.com</li>
        </ul>
      </div>

      <svg class="brand-disc" viewBox="0 0 400 400" aria-hidden="true">
        <circle cx="200" cy="200" r="168" fill="var(--plum)"/>
      </svg>
    </section>
  </main>
</body>
</html>
```